Employee Benefits Consulting Firm needs a refreshed website

I have a business (an employee benefits consulting firm) called Korvane Benefits Group, LLC (www.korvanebenefits-example.com).  The existing site is currently hosted on Plumhaven.  The business has been pretty much dormant since 2012.  I've relaunched the business and need a new website and looking for the website to be in Wordpress and to start with just 5 pages:
Home
About Us
Services
Contact Us
Blog
Some information about Korvane Benefits Group:
There is a tremendous waste (financial) in the traditional employee benefit model --- the current system is broken and simply stated, unsustainable. We take a very different approach when it comes to employee benefits consulting, constantly strive to provide short-term and long-term cost containment strategies that truly bend the healthcare cost curve... Many of our clients consider us as Benefit Architects...
Each employer/business is unique.
In short, our firm works with Employers to first understand their business.... -their history, their corporate structure, their leadership, their values, their uniqueness, etc.
Then we take a deep dive and get a strong grasp on their existing benefits program... -how did they get to where they are today, what are their goals/objectives, what is their risk tolerance, what are current pain points, are they compliant, etc.
Then after thorough analysis, we deliver a tailored solution. We implement the programs and manage the various aspects and moving parts of the program throughout the year.
We also are constantly analyzing the performance of the plan and monitor population health. We aggregate data and constantly refine the approach/strategy.

Updates
I made a few updates to the brief over the past couple of days...below is the updated brief:
Home
About Us
Services
Contact Us
Blog
MUST HAVE:
Mobile Friendly
PLEASE USE MERIDOX THEME
SHOULD HAVE:
the ability to add embedded video client testimonials
the ability for online chat
SHOULD NOT HAVE:
Photos from the old/existing website, I apologize for the late directive

I apologize for the delay on responding. Content is just about complete and will submit ASAP. Please let me know your availability to complete this project.

Updated content has been posted to this project.  I appreciate everybody's patience as we are working through this!

Target Market(s)
This is a BtoB website, primarily focusing on the following targets: CFOs, CEOs, Directors of Human Resources
Industry/Entity Type
Consulting
Number of Pages Required
5+ page
Requirements
Must have
- Mobile Friendly
- PLEASE USE MERIDOX THEME
Nice to have
- the ability to add embedded video client testimonials
- the ability for online chat
Should not have
- Photos from the old/existing website, I apologise for the late directive

```html
<!DOCTYPE html>
<html lang="en">
<head>
<meta charset="utf-8">
<title>Korvane Benefits Group</title>
<link rel="stylesheet" href="https://fonts.googleapis.com/css2?family=Merriweather:wght@700&family=Roboto:ital,wght@0,400;0,500;0,700;0,900;1,700&display=swap">
<style>
:root{
  --navy:#2a2a78;
  --purple:#3b2a8c;
  --accent:#e4401f;
  --panel:#b7bfca;
  --light:#eceef1;
  --white:#ffffff;
  --text:#555b66;
  --green:#2e9e3e;
  --phone:#a9c3e6;
  --logo-grey:#9a9a9a;
}
*{box-sizing:border-box;margin:0;padding:0}
html,body{width:769px;height:1200px;overflow:hidden;background:var(--white)}
body{position:relative;font-family:'Roboto',sans-serif;color:var(--text)}
.abs{position:absolute}
.serif{font-family:'Merriweather',serif}

/* hero */
.hero-photo{left:0;top:0;width:484px;height:259px;background:linear-gradient(120deg,#3d4a5e 0%,#6d7788 40%,#b9aea5 60%,#4a5468 100%)}
.hero-photo::after{content:"";position:absolute;inset:0;background:linear-gradient(180deg,rgba(40,50,70,0) 55%,rgba(40,50,70,.55) 100%)}
.brand{left:14px;top:20px;color:var(--white);font-family:'Roboto',sans-serif;font-weight:700;font-size:14px;display:flex;align-items:center;gap:6px}
.brand-mark{width:10px;height:10px;border-radius:50%;background:var(--white)}
.hero-title{left:15px;top:195px;color:var(--white);font-weight:700;font-size:17px}
.hero-rule{left:15px;top:219px;width:206px;height:1px;background:rgba(255,255,255,.8)}
.hero-sub{left:15px;top:236px;color:var(--accent);font-size:12.5px}

.form-panel{left:484px;top:0;width:285px;height:259px;background:var(--panel)}
.form-title{left:504px;top:32px;width:250px;color:var(--white);font-size:14.5px;line-height:16px}
.form-note{left:504px;top:95px;font-size:6px;color:#3a3f4a}
.field{left:504px;width:245px;background:var(--white);border:1px solid #d6d9de;font-size:5.5px;color:#8a8f98;padding:5px 6px}
.send{left:504px;top:203px;width:245px;height:24px;background:var(--purple);color:var(--white);font-size:7.5px;font-weight:700;letter-spacing:.8px;display:flex;align-items:center;justify-content:center}
.menu-btn{left:738px;top:4px;width:28px;height:25px;border:1px solid var(--green);background:var(--white);display:flex;align-items:center;justify-content:center}

/* process */
.step{top:279px;width:110px;text-align:center}
.step-icon{width:19px;height:19px;border-radius:50%;background:#1f4aa0;margin:0 auto;display:flex;align-items:center;justify-content:center}
.step h3{font-family:'Merriweather',serif;font-size:8.5px;color:var(--navy);margin-top:9px}
.step p{font-size:5.8px;line-height:9.6px;color:#333;margin-top:6px}

/* split sections */
.photo-meeting{left:0;top:384px;width:385px;height:248px;background:linear-gradient(100deg,#c9c2b8 0%,#6f7890 30%,#2d3550 55%,#7e8595 100%)}
.split-bg-right{left:385px;top:384px;width:384px;height:248px;background:var(--light)}
.split-bg-left{left:0;top:632px;width:385px;height:255px;background:var(--light)}
.photo-signing{left:385px;top:632px;width:384px;height:255px;background:linear-gradient(135deg,#2a2a2a 0%,#cfd1d4 25%,#f2f2f2 55%,#c8ccd0 80%,#3a3a3a 100%)}
.block h2{font-family:'Merriweather',serif;font-size:10px;color:var(--navy)}
.block .rule{width:38px;height:2px;background:var(--accent);margin-top:14px}
.block p{font-size:6.2px;line-height:9.6px;margin-top:11px;color:var(--text)}
.cta-btn{display:inline-flex;align-items:center;justify-content:center;width:126px;height:22px;background:var(--purple);color:var(--white);font-size:6.5px;font-weight:700;letter-spacing:.7px;margin-top:10px}

/* partners */
.partners{left:0;top:887px;width:769px;height:100px}
.partner{position:absolute;background:var(--logo-grey);opacity:.55}

/* call to action */
.cta-band{left:0;top:987px;width:769px;height:213px;background:linear-gradient(90deg,#4c566b 0%,#6d778a 40%,#a4acb8 65%,#d6dbe0 100%)}
.cta-title{left:155px;top:1028px;color:var(--white);font-weight:900;font-size:20.5px;line-height:22px;text-transform:uppercase}
.cta-line{left:155px;width:215px;height:2px;background:var(--phone)}
.cta-phone{left:160px;top:1128px;color:var(--phone);font-style:italic;font-weight:700;font-size:28px}
</style>
</head>
<body>

<!-- hero -->
<div class="abs hero-photo" role="img" aria-label="Two business people shaking hands"></div>
<div class="abs brand"><span class="brand-mark"></span>Korvane Benefits Group</div>
<div class="abs hero-title">Unique Solutions</div>
<div class="abs hero-rule"></div>
<div class="abs hero-sub serif">Managing People As An Investment, Not A Cost</div>

<div class="abs form-panel"></div>
<div class="abs form-title serif">Let us use our 100 years of combined experience to help your business succeed.</div>
<div class="abs form-note">Fill out the form and take the first step to benefiting your business</div>
<div class="abs field" style="top:112px;height:17px">Name</div>
<div class="abs field" style="top:135px;height:17px">Email</div>
<div class="abs field" style="top:157px;height:40px">Message</div>
<div class="abs send">Send message</div>
<div class="abs menu-btn">
  <svg width="16" height="12" viewBox="0 0 16 12"><rect y="0" width="16" height="2" fill="#2e9e3e"/><rect y="5" width="16" height="2" fill="#2e9e3e"/><rect y="10" width="16" height="2" fill="#2e9e3e"/></svg>
</div>

<!-- process -->
<div class="abs step" style="left:147px">
  <div class="step-icon"><svg width="9" height="8" viewBox="0 0 9 8"><rect x="1" y="4" width="1.5" height="4" fill="#fff"/><rect x="4" y="1" width="1.5" height="7" fill="#fff"/><rect x="7" y="3" width="1.5" height="5" fill="#fff"/></svg></div>
  <h3>Plan &amp; Analyze</h3>
  <p>Lorem ipsum dolor sit amet, consectetur adipiscing elit. Ut elit tellus, luctus nec ullamcorper mattis.</p>
</div>
<div class="abs step" style="left:269px">
  <div class="step-icon"><svg width="10" height="7" viewBox="0 0 10 7"><rect x="0.5" y="0.5" width="9" height="6" fill="none" stroke="#fff"/><rect x="2" y="2" width="6" height="3" fill="#fff"/></svg></div>
  <h3>Design &amp; Build</h3>
  <p>Lorem ipsum dolor sit amet, consectetur adipiscing elit. Ut elit tellus, luctus nec ullamcorper mattis.</p>
</div>
<div class="abs step" style="left:390px">
  <div class="step-icon"><svg width="10" height="7" viewBox="0 0 10 7"><path d="M1 5 L4 2 L6 4 L9 1" fill="none" stroke="#fff" stroke-width="1.2"/></svg></div>
  <h3>Implement</h3>
  <p>Lorem ipsum dolor sit amet, consectetur adipiscing elit. Ut elit tellus, luctus nec ullamcorper mattis.</p>
</div>
<div class="abs step" style="left:512px">
  <div class="step-icon"><svg width="10" height="7" viewBox="0 0 10 7"><rect x="0.5" y="0.5" width="9" height="6" fill="none" stroke="#fff"/><rect x="2" y="2" width="6" height="3" fill="#fff"/></svg></div>
  <h3>Manage Year Round</h3>
  <p>Lorem ipsum dolor sit amet, consectetur adipiscing elit. Ut elit tellus, luctus nec ullamcorper mattis.</p>
</div>

<!-- split: control -->
<div class="abs photo-meeting" role="img" aria-label="Business team in a meeting"></div>
<div class="abs split-bg-right"></div>
<div class="abs block" style="left:423px;top:453px;width:290px">
  <h2>More Control. More Care. More Savings.</h2>
  <div class="rule"></div>
  <p>To create a one-of-a-kind plan designed just for your business, you need a benefits partner that offers a one-of-a-kind discovery and implementation process. That's why we created a proprietary four-step guide, all designed to help ensure clients a tailor-made plan that meets their objectives, and stays well within their cost constraints.</p>
  <span class="cta-btn">GET FREE CONSULTATION</span>
</div>

<!-- split: ground -->
<div class="abs split-bg-left"></div>
<div class="abs photo-signing" role="img" aria-label="Hand signing a contract with a fountain pen"></div>
<div class="abs block" style="left:38px;top:696px;width:280px">
  <h2>Covering More Ground For You</h2>
  <div class="rule"></div>
  <p>At Korvane Benefits, we excel at identifying current plan weaknesses, opportunities for revisions and typically overlooked details – details that can make all the difference in your benefits strategy and associated costs. Our blend of strategic thinking and pro-active planning merges with our vast resources and cutting-edge technology to provide a solution that's both uncommon in method and unparalleled in value.</p>
  <span class="cta-btn">GET FREE CONSULTATION</span>
</div>

<!-- partners -->
<div class="abs partners" aria-label="Partner badges">
  <div class="partner" style="left:160px;top:27px;width:24px;height:30px"></div>
  <div class="partner" style="left:254px;top:35px;width:50px;height:14px"></div>
  <div class="partner" style="left:372px;top:27px;width:26px;height:26px;border-radius:50%"></div>
  <div class="partner" style="left:467px;top:34px;width:50px;height:14px"></div>
  <div class="partner" style="left:577px;top:25px;width:43px;height:36px"></div>
</div>

<!-- call to action -->
<div class="abs cta-band" role="img" aria-label="Smiling businessman in a bright office"></div>
<div class="abs cta-title">Take charge of<br>your benefit<br>program now</div>
<div class="abs cta-line" style="top:1126px"></div>
<div class="abs cta-phone">(555) 014-2780</div>
<div class="abs cta-line" style="top:1168px"></div>

</body>
</html>
```